Investment Fund Investor newsletter

I deleted the tear sheet example which was provided for design purposes only and not for content. Please see the simple outline for the newsletter and the related sections.

Please be clear this project is for a newsletter template. This means a template that can be updated on a monthly or quarterly basis with new content for our audience. Sections should include: Operations Update, Financial Update, Energy Investor News.

We need a template for a newsletter that can be sent out in Word format and also able to send out via Mailchimp. Audience are current investors in our oil and gas fund. These investors are high net worth individuals and private equity firms so the branding needs to be high end, sophisticated and corporate. Please see website and attached tear sheet for the type of branding that we want to match. Website is www.brambleford-power.com
Please see website and tear sheet for the color scheme that we want.

Target Market(s)

Our current fund investors that include high net worth investors and CEOs of private equity companies

Industry/Entity Type

oil and gas... investment

Font styles to use
Serif

Requirements
Must have
• Word file and can send via Mailchimp too

```html
<!DOCTYPE html>
<html lang="en">
<head>
<meta charset="utf-8">
<title>Brambleford Power Partners — Investor Newsletter</title>
<link rel="stylesheet" href="https://fonts.googleapis.com/css2?family=Poppins:wght@400;500;600;700&family=Cinzel:wght@500&display=swap">
<style>
  :root {
    --ink: #1f1f1f;
    --body: #555555;
    --accent: #56c6f0;
    --white: #ffffff;
    --footer: #2b2b2b;
    --hero-dark: #1d1718;
    --hero-warm: #5a3a2c;
  }
  * { margin: 0; padding: 0; box-sizing: border-box; }
  html, body { width: 1200px; height: 3212px; overflow: hidden; background: var(--white); }
  body { position: relative; font-family: "Poppins", sans-serif; color: var(--ink); }

  .hero {
    position: absolute; left: 0; top: 0; width: 1200px; height: 732px;
    background: radial-gradient(ellipse 70% 45% at 50% 35%, var(--hero-warm) 0%, #35241f 45%, var(--hero-dark) 100%);
    display: flex; align-items: center; justify-content: center;
  }
  .brand-name {
    color: var(--white); font-family: "Poppins", sans-serif; font-weight: 500;
    font-size: 34px; letter-spacing: 8px; text-align: center; line-height: 1.5;
    margin-top: -20px;
  }

  .section-title {
    position: absolute; left: 0; width: 1200px; text-align: center;
    font-weight: 700; font-size: 62px; line-height: 1; color: var(--ink);
  }
  .rule { position: absolute; left: 533px; width: 135px; height: 4px; background: var(--accent); }
  .rule--dark { background: var(--ink); }

  .feature { position: absolute; top: 944px; width: 350px; text-align: center; }
  .feature svg { display: block; margin: 0 auto; width: 104px; height: 104px; }
  .feature h3 { margin-top: 38px; font-weight: 500; font-size: 23px; color: var(--ink); }
  .feature p { margin-top: 14px; font-size: 19px; line-height: 36.6px; color: var(--body); }

  .team-band { position: absolute; left: 0; top: 1295px; width: 1200px; height: 366px; background: var(--accent); }
  .member { position: absolute; top: 1529px; width: 351px; text-align: center; }
  .member .portrait {
    width: 351px; height: 366px;
    background: linear-gradient(160deg, #bdbdbd 0%, #8a8a8a 55%, #3a3a3a 100%);
    box-shadow: 0 2px 10px rgba(0,0,0,0.18);
  }
  .member h4 { margin-top: 26px; font-weight: 600; font-size: 26px; color: var(--ink); }
  .member p { margin-top: 4px; font-size: 20px; line-height: 38px; color: var(--body); }

  .about-text {
    position: absolute; left: 58px; top: 2214px; width: 1086px;
    text-align: center; font-size: 20px; line-height: 41px; color: var(--body);
  }
  .photo { position: absolute; }
  .photo--sunset {
    left: 51px; top: 2384px; width: 829px; height: 477px;
    background: linear-gradient(180deg, #1f3fa8 0%, #3b5ab8 35%, #c95a3a 68%, #f2801e 85%, #2a1a14 100%);
  }
  .photo--rig {
    left: 565px; top: 2574px; width: 579px; height: 479px;
    background: linear-gradient(135deg, #8fa6d6 0%, #c9d3e6 40%, #6b6862 70%, #3b3835 100%);
    box-shadow: 0 4px 14px rgba(0,0,0,0.25);
  }

  .footer {
    position: absolute; left: 0; top: 3110px; width: 1200px; height: 102px;
    background: var(--footer); color: var(--white);
    display: flex; align-items: center; justify-content: center; font-size: 23px;
  }
</style>
</head>
<body>

<header class="hero" role="img" aria-label="Oil pumpjacks and drilling derricks silhouetted against a dusk sky">
  <div class="brand-name">BRAMBLEFORD<br>POWER PARTNERS</div>
</header>

<h2 class="section-title" style="top:786px;">Why Choose Us</h2>
<div class="rule" style="top:883px;"></div>

<div class="feature" style="left:40px;">
  <svg viewBox="0 0 104 104" fill="none" stroke="#56c6f0" stroke-width="3" stroke-linecap="round" stroke-linejoin="round">
    <line x1="6" y1="98" x2="100" y2="98"/>
    <path d="M40 98 L52 30 L64 98"/>
    <line x1="45" y1="70" x2="59" y2="70"/>
    <line x1="42" y1="85" x2="62" y2="85"/>
    <line x1="16" y1="22" x2="88" y2="28"/>
    <rect x="82" y="12" width="12" height="40" rx="3"/>
    <line x1="20" y1="22" x2="20" y2="80"/>
    <circle cx="20" cy="84" r="6"/>
  </svg>
  <h3>Operations Update</h3>
  <p>Lorem ipsum dolor sit consectetur adipiscing elit, Iminim veniam, quis nostrud exercitation ullamco</p>
</div>

<div class="feature" style="left:422px;">
  <svg viewBox="0 0 104 104" fill="none" stroke="#56c6f0" stroke-width="3" stroke-linecap="round" stroke-linejoin="round">
    <circle cx="52" cy="52" r="46"/>
    <line x1="52" y1="52" x2="52" y2="6"/>
    <line x1="52" y1="52" x2="92" y2="74"/>
    <line x1="52" y1="52" x2="12" y2="74"/>
    <circle cx="70" cy="28" r="11"/>
    <text x="70" y="34" text-anchor="middle" font-size="16" fill="#56c6f0" stroke="none" font-family="Poppins, sans-serif">$</text>
    <text x="32" y="44" text-anchor="middle" font-size="20" fill="#56c6f0" stroke="none" font-family="Poppins, sans-serif">$</text>
    <line x1="42" y1="92" x2="42" y2="78"/>
    <line x1="52" y1="92" x2="52" y2="68"/>
    <line x1="62" y1="92" x2="62" y2="82"/>
  </svg>
  <h3>Financial Update</h3>
  <p>Lorem ipsum dolor sit consectetur adipiscing elit, Iminim veniam, quis nostrud exercitation ullamco</p>
</div>

<div class="feature" style="left:803px;">
  <svg viewBox="0 0 104 104" fill="none" stroke="#56c6f0" stroke-width="3" stroke-linecap="round" stroke-linejoin="round">
    <circle cx="54" cy="52" r="18"/>
    <path d="M58 40 L48 54 H58 L50 66"/>
    <path d="M20 14 C40 8 60 10 84 10 M30 26 C45 20 60 18 84 20"/>
    <path d="M20 90 C40 96 60 94 84 94 M30 78 C45 84 60 86 84 84"/>
  </svg>
  <h3>Energy Investor News</h3>
  <p>Lorem ipsum dolor sit consectetur adipiscing elit, Iminim veniam, quis nostrud exercitation ullamco</p>
</div>

<div class="team-band"></div>
<h2 class="section-title" style="top:1376px;">Meet Our Team</h2>
<div class="rule rule--dark" style="top:1461px;"></div>

<div class="member" style="left:50px;">
  <div class="portrait" role="img" aria-label="Black and white portrait of the managing partner"></div>
  <h4>Gordon Hailey</h4>
  <p>Managing Partner</p>
</div>
<div class="member" style="left:424px;">
  <div class="portrait" role="img" aria-label="Black and white portrait of a partner"></div>
  <h4>Nathan Kerrow</h4>
  <p>Partner</p>
</div>
<div class="member" style="left:797px;">
  <div class="portrait" role="img" aria-label="Black and white portrait of the finance and administration partner"></div>
  <h4>Diane Hailey</h4>
  <p>Partner — Finance and<br>Administration</p>
</div>

<h2 class="section-title" style="top:2097px;">About Us</h2>
<div class="rule" style="top:2183px;"></div>
<p class="about-text">We are a diverse team of professionals with over 100 years of combined experience in oil and gas. We are uniquely positioned to take advantage of opportunities in the conventional oil and gas space and are fully supported by the dedicated operating experience of KTR Field Services.</p>

<div class="photo photo--sunset" role="img" aria-label="Pumpjack silhouetted against a blue and orange sunset sky"></div>
<div class="photo photo--rig" role="img" aria-label="Drilling rig beside a stack of steel pipes under a cloudy sky"></div>

<footer class="footer">© 2022 All Rights Reserved</footer>

</body>
</html>
```